STOREFRONT LIT SIGN for The Ranchera Loft

A sign advertising our music academy. This sign will be hung 10 feet above the entrance of our building and will be seen by all pedestrian and vehicle traffic on Birch Lane Delano.

Target Market(s)

Street passerby

Industry/Entity Type

Music Training

Font styles to use
Other font styles liked:
• Creative

Colors

Designer to choose colors to be used in the design.

Requirements
Must have
• A White Background
• Dimensions: 8 ft long x 3 ft tall
• The Ranchera Loft of Delano
• Lecciones de Piano, Violin, Guitarra, Voz, Trompeta y Mas
• MUSIC ACADEMY *(This should be most prominent)
• Guitar, Voice, Trumpet and More
• (661) 555-0147
• therancheraloft.example
Nice to have
• Graphics of a piano, or guitar, or violin or trumpet or a combination of two or more

```html
<!DOCTYPE html>
<html lang="en">
<head>
<meta charset="utf-8">
<title>The Ranchera Loft of Delano – Music Academy Sign</title>
<link rel="stylesheet" href="https://fonts.googleapis.com/css2?family=Montserrat:wght@600;700;800&display=swap">
<style>
  :root {
    --sign-red: #7d0000;
    --frame-red: #6b0000;
    --text-gray: #808080;
    --icon-gray: #d4d4d4;
    --paper: #ffffff;
  }
  html, body {
    margin: 0;
    padding: 0;
    width: 1200px;
    height: 1200px;
    overflow: hidden;
    background: var(--paper);
  }
  .canvas {
    position: relative;
    width: 1200px;
    height: 1200px;
  }
  .sign {
    position: absolute;
    left: 0;
    top: 0;
    width: 1200px;
    height: 1200px;
    font-family: "Montserrat", sans-serif;
  }
  .sign-frame { fill: var(--paper); stroke: var(--frame-red); stroke-width: 14; }
  .studio-name { fill: var(--text-gray); font-weight: 700; font-size: 38px; }
  .academy-title { fill: var(--sign-red); font-weight: 800; }
  .lessons-line { fill: var(--text-gray); font-weight: 700; font-size: 24px; }
  .phone { fill: var(--sign-red); font-weight: 700; font-size: 48px; }
  .website { fill: var(--text-gray); font-weight: 700; font-size: 30px; }
  .instrument { fill: var(--icon-gray); }
</style>
</head>
<body>
<main class="canvas">
  <svg class="sign" viewBox="0 0 1200 1200" xmlns="http://www.w3.org/2000/svg">
    <rect class="sign-frame" x="175" y="283" width="850" height="310"/>

    <text class="studio-name" x="600" y="328" text-anchor="middle" textLength="595" lengthAdjust="spacingAndGlyphs">The Ranchera Loft of Delano</text>

    <text class="academy-title" x="206" y="416" textLength="796" lengthAdjust="spacingAndGlyphs"><tspan font-size="116">M</tspan><tspan font-size="86">USIC </tspan><tspan font-size="116">A</tspan><tspan font-size="86">CADEMY</tspan></text>

    <text class="lessons-line" x="206" y="446" textLength="792" lengthAdjust="spacingAndGlyphs">Lecciones de Piano, Violin, Guitarra, Voz, Trompeta y Mas</text>

    <rect class="instrument" x="200" y="462" width="92" height="120" rx="6" role="img" aria-label="Grand piano silhouette"/>
    <rect class="instrument" x="310" y="460" width="86" height="120" rx="6" role="img" aria-label="Violin silhouette"/>

    <text class="phone" x="414" y="528" textLength="376" lengthAdjust="spacingAndGlyphs">(661) 555-0147</text>
    <text class="website" x="410" y="572" textLength="384" lengthAdjust="spacingAndGlyphs">therancheraloft.example</text>

    <rect class="instrument" x="822" y="460" width="84" height="120" rx="6" role="img" aria-label="Acoustic guitar silhouette"/>
    <rect class="instrument" x="920" y="460" width="76" height="122" rx="6" role="img" aria-label="Trumpet silhouette"/>
  </svg>
</main>
</body>
</html>
```